RUXO9 biz card & Stationery

UXO9 is a personalized shopping experience brought to you, that lets you find and discover fashion goods through a collection of boutiques curated by taste-makers - celebrities, stylists, designers, and fashion bloggers. Boutiques uses visual technology to help fashionistas discover and shop their look and creates the opportunity for designers to showcase their collections and latest inspirations online.

RUXO9 is built on technology developed by our team of fashion experts who work with engineers to “teach” our computer systems to understand various patterns, pairings, and genre definitions. When signed into your account, RUXO9 learns about your style and preferences and in turn, provides you better results and recommendations over time. Ultimately, RUXO9 will provide shoppers with a much richer and interactive shopping experience and help drive traffic to retailers' websites.

We need a definitely cool business card. The card must be black! And must use our official logo which can be download from RUXO9.com

The address for Letter head and evenlop, please use 4821 Larkmoor Avenue, Sutie 520 Los Angeles CA90012, email will be anyone@RUXO9.com, website is www.RUXO9.com

thanks

We received some of the design, thanks. But most of the design are not what we want. We need a very clean version with black ground, you may also use some dark gray to add the element. please take a look at http://bleckvorn.no/work/#tarvik__olmstrup/, we do like this kind of design very much. hope it help.

```html
<!DOCTYPE html>
<html lang="en">
<head>
<meta charset="utf-8">
<title>RUXO9 Letterhead</title>
<link href="https://fonts.googleapis.com/css2?family=Cinzel:wght@700&family=Marcellus&display=swap" rel="stylesheet">
<style>
  :root {
    --backdrop: #a9a9a9;
    --paper: #ffffff;
    --ink-black: #000000;
    --band-dark-gray: #2b2b2b;
    --logo-white: #ffffff;
    --address-ink: #111111;
    --watermark-gray: #f0f0f0;
  }
  * { margin: 0; padding: 0; box-sizing: border-box; }
  html, body {
    width: 1200px;
    height: 900px;
    overflow: hidden;
    background: var(--backdrop);
  }
  .letterhead {
    position: absolute;
    left: 291px;
    top: 50px;
    width: 618px;
    height: 800px;
    background: var(--paper);
    overflow: hidden;
  }
  .header-band {
    position: absolute;
    left: 0; top: 0;
    width: 100%;
    height: 60px;
    background: linear-gradient(90deg, var(--ink-black) 25%, var(--band-dark-gray) 100%);
  }
  .brand-name {
    position: absolute;
    right: 15px;
    top: 11px;
    font-family: "Marcellus", serif;
    font-size: 37px;
    line-height: 1;
    color: var(--logo-white);
    letter-spacing: 0.5px;
  }
  .address-line {
    position: absolute;
    right: 16px;
    top: 64px;
    font-family: "Cinzel", serif;
    font-weight: 700;
    font-size: 10.5px;
    color: var(--address-ink);
    letter-spacing: 0.3px;
    white-space: nowrap;
  }
  .brand-watermark {
    position: absolute;
    right: 16px;
    bottom: 36px;
    font-family: "Marcellus", serif;
    font-size: 90px;
    line-height: 1;
    color: var(--watermark-gray);
  }
  .footer-band {
    position: absolute;
    left: 0; bottom: 0;
    width: 100%;
    height: 30px;
    background: var(--ink-black);
  }
</style>
</head>
<body>
  <div class="letterhead">
    <header class="header-band">
      <div class="brand-name">RUXO9</div>
    </header>
    <p class="address-line">Larkmoor Avenue, Suite 520 - Los Angeles CA90012</p>
    <div class="brand-watermark" aria-hidden="true">RUXO9</div>
    <footer class="footer-band"></footer>
  </div>
</body>
</html>
```